Website design for headhunting agency

The design I need (PSD file) is for a company offering specialised services in recruitment of high-end executive and management positions for businesses.
OBJECTIVES OF THE WEBSITE:
1. Let entrepreneurs and business leaders know about their services and easily have them contact Velnarix if they want more information about their services.
2. Display a list of available carreer opportunities (according to their client's need).
WHAT I NEED:
1st, I need the design for the Home Page ONLY. Once approved, I will need the other pages designed as well. (Here is prototype that we've already developed for the Website that will guide you in the design:
http://demo.quorvaweb.example/velnarix/fr/accueil)
ATTACHED FILES
- Logo
- PDF brochure: Use for inspiration. It is encouraged that you use pictures from this brochure. You can always suggest new ones, as long as they are not expensive to buy and have the same look and feel as the brochure.
HOMEPAGE:
1. Main menu : 6 sections
Accueil | Velnarix | Équipe | Approche | Postes disponibles | Publications
2. Main slider: 4 sections
- Chasseurs de têtes (Headhunters)
- Notre approche (Our Approach)
- Postes cadres disponibles (Executive Careers
Opportunities)
- Contactez-nous (Contact Us)
3. Main Call To Action Boxes :
- Liste Des postes disponibles (Liste of Available Careers
Opportunities)
- Formulaire de contact (contact form)
4. Latest blog articles
- Les derniers articles.
OTHER PAGES (to design once Homepage is approved)
- Velnarix (about us)
- Équipe (our team)
- Approche (our approach)
- Postes disponibles (Career opportunities)
- Publications (blog articles)
- Contact (Contact us)
Target Market(s)
ORGANIZATIONS:
Leaders of organizations seeking to recruit highly qualified staff.
HIGHLY QUALIFIED RESOURCES:
Senior individuals seeking a salary between $70,000 and $ $200,000 annually
PROFESSIONAL SECTORS:
manufacturing : Primary and secondary industries
pharmaceutical
Aerospace
Finances
Retail business
Engineering
Chemical and petrochemical
IT, telecommunications and high technology
Professional Organizations and Association
Industry/Entity Type
Business
Look and feel
Each slider illustrates characteristics of the customer's brand and the style your logo design should communicate.

```html
<!DOCTYPE html>
<html lang="fr">
<head>
<meta charset="utf-8">
<title>Velnarix – Recherche de cadres</title>
<link href="https://fonts.googleapis.com/css2?family=Open+Sans:wght@400;600;700&display=swap" rel="stylesheet">
<style>
  :root {
    --teal-dark: #063f4a;
    --teal: #0b5f6e;
    --teal-mid: #0f7080;
    --orange: #e59a1c;
    --ink: #1d1d1d;
    --body: #8a8a8a;
    --rule: #d9d9d9;
    --white: #ffffff;
    --btn: #1b1b1b;
    --link: #0c5e6d;
    --hero-grey: #b9c0bc;
    --hero-light: #eef0ee;
    --hero-green: #7f9a78;
    --hero-warm: #d9c2b0;
    --hero-dark: #2b2b2e;
  }
  * { box-sizing: border-box; margin: 0; padding: 0; }
  html, body { width: 703px; height: 1200px; overflow: hidden; }
  body { font-family: "Open Sans", Arial, sans-serif; background: var(--white); color: var(--ink); position: relative; }

  .utility-bar {
    position: absolute; top: 0; left: 0; width: 703px; height: 23px;
    background: linear-gradient(var(--teal-mid), var(--teal-dark));
  }
  .utility-bar ul { list-style: none; display: flex; position: absolute; left: 187px; right: 0; height: 23px; }
  .utility-bar li {
    flex: 1; text-align: center; color: var(--white); font-size: 10px; font-weight: 600;
    line-height: 23px; letter-spacing: .4px; border-left: 1px solid rgba(255,255,255,.35);
  }
  .utility-bar li:first-child { border-left: none; }

  .site-header { position: absolute; top: 23px; left: 0; width: 703px; height: 89px; }
  .brand { position: absolute; left: 17px; top: 22px; }
  .brand-row { display: flex; align-items: center; gap: 8px; }
  .brand-mark { width: 14px; height: 14px; background: var(--orange); }
  .brand-name { font-size: 30px; font-weight: 600; color: var(--teal); letter-spacing: 1px; line-height: 1; }
  .brand-tagline { font-size: 11px; color: #555; margin-left: 66px; margin-top: 4px; }
  .main-nav { position: absolute; right: 14px; top: 39px; display: flex; align-items: center; }
  .main-nav a { font-size: 11.5px; font-weight: 600; color: var(--teal); text-decoration: none; letter-spacing: .3px; }
  .main-nav a.current { color: var(--orange); }
  .main-nav .sep { color: var(--teal); margin: 0 10px; font-size: 12px; }

  .hero {
    position: absolute; top: 112px; left: 0; width: 703px; height: 273px; overflow: hidden;
    background:
      linear-gradient(180deg, rgba(255,255,255,0) 55%, rgba(246,244,242,.85) 100%),
      linear-gradient(90deg,
        var(--hero-grey) 0%, var(--hero-light) 12%, var(--hero-warm) 22%,
        var(--hero-light) 32%, var(--hero-green) 42%, var(--hero-light) 50%,
        var(--hero-warm) 58%, var(--hero-light) 66%, var(--hero-light) 74%,
        var(--hero-dark) 84%, var(--hero-dark) 100%);
  }
  .hero-arrow { position: absolute; top: 124px; }
  .hero-arrow.prev { left: 8px; }
  .hero-arrow.next { right: 8px; }
  .slider-dots { position: absolute; top: 403px; left: 322px; display: flex; gap: 6px; }
  .slider-dots span { width: 9px; height: 9px; border-radius: 50%; background: #c8c8c8; }
  .slider-dots span.active { background: var(--teal); }

  .cta-box { position: absolute; top: 434px; width: 329px; height: 190px; border: 1px solid var(--rule); }
  .cta-box.jobs { left: 15px; }
  .cta-box.contact { left: 359px; }
  .cta-box h2 { font-size: 13.5px; font-weight: 400; letter-spacing: .3px; position: absolute; left: 9px; top: 14px; }
  .job-list { list-style: none; position: absolute; left: 29px; top: 42px; }
  .job-list li { font-size: 11px; color: var(--link); line-height: 16.5px; display: flex; align-items: center; }
  .job-list li::before {
    content: ""; width: 0; height: 0; border-left: 7px solid #222; border-top: 4px solid transparent;
    border-bottom: 4px solid transparent; margin-right: 12px;
  }
  .field { position: absolute; left: 35px; display: flex; align-items: center; }
  .field label { font-size: 12px; color: var(--teal); width: 92px; }
  .field span.input { width: 166px; height: 22px; border: 1px solid #cfcfcf; }
  .field.user { top: 61px; }
  .field.pass { top: 106px; }

  .btn {
    position: absolute; display: flex; align-items: center; gap: 6px;
    height: 21px; padding: 0 11px 0 8px; background: linear-gradient(#3a3a3a, var(--btn));
    border-radius: 4px; color: var(--white); font-size: 10.5px; font-weight: 600;
  }
  .btn::before {
    content: ""; border-left: 6px solid var(--white); border-top: 3.5px solid transparent; border-bottom: 3.5px solid transparent;
  }
  .cta-box .btn { left: 29px; top: 153px; }
  .cta-box.contact .btn { left: 35px; padding-right: 24px; }

  .articles-rule { position: absolute; top: 642px; left: 0; width: 703px; border-top: 1px solid var(--rule); }
  .articles-title { position: absolute; top: 650px; left: 24px; font-size: 13.5px; font-weight: 400; letter-spacing: .3px; }

  .article-card { position: absolute; width: 319px; height: 190px; border: 1px solid var(--rule); }
  .article-card .thumb { position: absolute; left: 3px; top: 12px; width: 120px; height: 77px; border: 3px solid #eee; }
  .article-card .intro { position: absolute; left: 135px; top: 11px; width: 175px; font-size: 8.8px; line-height: 14.5px; color: var(--body); }
  .article-card .full { position: absolute; left: 3px; top: 100px; width: 305px; font-size: 8.8px; line-height: 14.5px; color: var(--body); }
  .article-card .btn { left: 1px; top: 157px; }
  .card-1 { left: 24px; top: 676px; }
  .card-2 { left: 368px; top: 676px; }
  .card-3 { left: 24px; top: 884px; }
  .card-4 { left: 368px; top: 884px; }
  .thumb.meeting { background: linear-gradient(135deg, #c9b9a6, #eae4dc 60%, #9aa0a6); }
  .thumb.plans { background: linear-gradient(135deg, #e8eef2, #f6f8fa 55%, #b8c8d4); }
  .thumb.team { background: linear-gradient(135deg, #c58a3e, #e7d8c4 55%, #8c5a46); }
  .thumb.office { background: linear-gradient(135deg, #dde6ea, #f3f5f6 55%, #6d7479); }

  .social-row { position: absolute; top: 1104px; left: 0; width: 703px; height: 34px; }
  .social-label { position: absolute; top: 9px; font-size: 13px; display: flex; align-items: center; gap: 6px; }
  .social-label::before {
    content: ""; border-left: 6px solid var(--teal); border-top: 3.5px solid transparent; border-bottom: 3.5px solid transparent;
  }
  .social-label.follow { left: 21px; }
  .social-label.newsletter { left: 365px; }
  .badge { position: absolute; top: 0; height: 34px; border: 1px solid #cfcfcf; display: flex; align-items: center; justify-content: center; font-weight: 700; color: var(--teal); }
  .badge.network { left: 217px; width: 87px; font-size: 13px; }
  .badge.signup { left: 598px; width: 88px; font-size: 16px; }

  .footer-rule { position: absolute; top: 1161px; left: 0; width: 703px; border-top: 2px solid var(--teal); }
  .site-footer {
    position: absolute; top: 1170px; left: 0; width: 703px; height: 30px;
    background: linear-gradient(var(--teal-mid), var(--teal-dark)); color: var(--white);
    font-size: 9.5px; display: flex; justify-content: space-between; align-items: center; padding: 0 15px 0 25px;
  }
  .site-footer strong { font-weight: 600; }
</style>
</head>
<body>
  <nav class="utility-bar">
    <ul>
      <li>ACCUEIL</li><li>PLAN DU SITE</li><li>CODE D'ÉTIQUE</li><li>CONTACT</li><li>ENGLISH</li>
    </ul>
  </nav>

  <header class="site-header">
    <div class="brand">
      <div class="brand-row"><span class="brand-mark"></span><span class="brand-name">VELNARIX</span></div>
      <div class="brand-tagline">Recherche de cadres</div>
    </div>
    <nav class="main-nav">
      <a class="current">À PROPOS</a><span class="sep">|</span>
      <a>ÉQUIPE</a><span class="sep">|</span>
      <a>APPROCHE</a><span class="sep">|</span>
      <a>POSTES DISPONIBLES</a><span class="sep">|</span>
      <a>PUBLICATIONS</a>
    </nav>
  </header>

  <section class="hero" role="img" aria-label="Photo d'une équipe de cinq cadres souriants en chemises claires et vestons foncés, devant un bureau lumineux avec des plantes vertes">
    <svg class="hero-arrow prev" width="14" height="22" viewBox="0 0 14 22"><polyline points="11,2 3,11 11,20" fill="none" stroke="#fff" stroke-width="3"/></svg>
    <svg class="hero-arrow next" width="14" height="22" viewBox="0 0 14 22"><polyline points="3,2 11,11 3,20" fill="none" stroke="#fff" stroke-width="3"/></svg>
  </section>
  <div class="slider-dots"><span class="active"></span><span></span><span></span><span></span></div>

  <section class="cta-box jobs">
    <h2>LISTE DES POSTES DISPONIBLES</h2>
    <ul class="job-list">
      <li>Aonecqua mfelisuame</li>
      <li>Bonecqua mfeluame</li>
      <li>Conecqua mame</li>
      <li>Doneiua feuame</li>
      <li>Enecqua rhlisuame</li>
      <li>FAonecqua yrelisume</li>
    </ul>
    <span class="btn">View More</span>
  </section>

  <section class="cta-box contact">
    <h2>FORMULAIRE DE CONTACT</h2>
    <div class="field user"><label>User Name</label><span class="input"></span></div>
    <div class="field pass"><label>Password</label><span class="input"></span></div>
    <span class="btn">Login</span>
  </section>

  <div class="articles-rule"></div>
  <h2 class="articles-title">LES DERNIERS ARTICLES</h2>

  <article class="article-card card-1">
    <div class="thumb meeting" role="img" aria-label="Photo de collègues en réunion autour d'un ordinateur"></div>
    <p class="intro">Donec quam felis, ultricies nec, pellentesque eu, pretium quis, sem. Nulla consequat massa quis enim. Donec pede justo, fringilla vel, aliquet nec, vulputate eget, arcu.</p>
    <p class="full">Donec quam felis, ultricies nec, pellentesque eu, pretium quis, sem. Nulla consequat massa quis enim. Donec pede justo, fringilla vel, aliquet nec, vulputate eget, arcu.</p>
    <span class="btn">View More</span>
  </article>
  <article class="article-card card-2">
    <div class="thumb plans" role="img" aria-label="Photo de plans techniques enroulés sur un bureau"></div>
    <p class="intro">Donec quam felis, ultricies nec, pellentesque eu, pretium quis, sem. Nulla consequat massa quis enim. Donec pede justo, fringilla vel, aliquet nec, vulputate eget, arcu.</p>
    <p class="full">Donec quam felis, ultricies nec, pellentesque eu, pretium quis, sem. Nulla consequat massa quis enim. Donec pede justo, fringilla vel, aliquet nec, vulputate eget, arcu.</p>
    <span class="btn">View More</span>
  </article>
  <article class="article-card card-3">
    <div class="thumb team" role="img" aria-label="Photo d'une équipe d'affaires discutant ensemble"></div>
    <p class="intro">Donec quam felis, ultricies nec, pellentesque eu, pretium quis, sem. Nulla consequat massa quis enim. Donec pede justo, fringilla vel, aliquet nec, vulputate eget, arcu.</p>
    <p class="full">Donec quam felis, ultricies nec, pellentesque eu, pretium quis, sem. Nulla consequat massa quis enim. Donec pede justo, fringilla vel, aliquet nec, vulputate eget, arcu.</p>
    <span class="btn">View More</span>
  </article>
  <article class="article-card card-4">
    <div class="thumb office" role="img" aria-label="Photo de cadres dans un bureau moderne"></div>
    <p class="intro">Donec quam felis, ultricies nec, pellentesque eu, pretium quis, sem. Nulla consequat massa quis enim. Donec pede justo, fringilla vel, aliquet nec, vulputate eget, arcu.</p>
    <p class="full">Donec quam felis, ultricies nec, pellentesque eu, pretium quis, sem. Nulla consequat massa quis enim. Donec pede justo, fringilla vel, aliquet nec, vulputate eget, arcu.</p>
    <span class="btn">View More</span>
  </article>

  <section class="social-row">
    <span class="social-label follow">SUIVEZ-NOUS SUR NEXALINK</span>
    <span class="badge network">Nexalink</span>
    <span class="social-label newsletter">INSCRIVEZ-VOUS À L'INFOLETTRE</span>
    <span class="badge signup">Sign Up</span>
  </section>

  <div class="footer-rule"></div>
  <footer class="site-footer">
    <strong>© Velnarix – Tous droits réservés</strong>
    <span>Site Web et stratégie Agence de Développement Internet</span>
  </footer>
</body>
</html>
```